IT Company Business Card Design w/Stationary Design

We have a great logo we like! We are looking to redesign our business cards and all company logo'd merchandise/materials.

We are an IT Company located near the Bay Area (San Francisco, CA). We specialize in Managed Services and offer complete IT Computer and Network Support to Businesses of all sizes. We thrive on making a lasting impression. We have been doing IT for 15yrs+ but are young at heart. We like to stand out and be different. We want to be unique and have a recognizable brand. We need our logo to represent who we are. We are young, professional, creative and outstanding. We don't want to blend in, we want to stand out. Our business card needs to stand out and grab attention. Something Bold, yet simple and clean. (I will provide ideas of what we like to give a taste of what we are looking for).

The design can include any kind of texture/artistic design or sizing EXCEPT please "no square card designs" as they don't seem to fit in wallets very well. We dont mind curved edges, rounded corners, vertical layouts or horizontal layouts, embossing, letter press or raised surfaces. Again, we dont want to look average or plain or boring. :) Be creative - yet practical! We have ordered from Pebblecraft designs before and been very happy. Their card sizes tend to be a little different, so beware. Hope this helps!

Target Market(s)

Businesses - Small to Medium, Corporations, Publicly Traded Companies

Industry/Entity Type

Business

Contact Information for Business Card

Harbor Lantern IT
7318 Quillby Avenue
Suite F
Alderton, CA 95871

Office 530.555.0137
Direct 530.555.0182
Cell 530.555.0164

Ross Tavener
Founder, CEO
www.hlit-example.com
rtavener@hlit-example.com

Locations Serviced: Alderton, Brookmere, Ridgeport, Fallow (incorporate this on the card ONLY if there's a good place to do so).

What we specialize in: Computer, Network, Voice, Data. (IT Services)

Our Logo Colors: Black and Blue (#006699). Open to using grey or orange as well - but not required. Don't want too busy....

Logo Font: "Cinthe" (Will attach logo font). We want type style to be clean. You can show different font types including our logo font - and we are open to other font ideas.

The logo can be separated. You can use elements together or apart. Surprise us! :) We "REALLY" want the "hl" to be our identifier/our brand people recognize.

Font styles to use
Sans Serif

Colors
0355a3
3176b5
f37122
f78f20
faa54b
474747
aaaaaa
757575
000000

Requirements
Must have
• Bold, Big, Colorful, Modern/yet Fun, Clean Design, Stand Out Presence, Texture would be welcomed - but not necessary, Card design shape can include cut corners or rounded or square edges. Be creative. (HOWEVER, we don't want a square design because we have found it doesn't fit in wallets that easily).
• We do like using Pebblecraft printing company (Which they have particular sizing on their card templates - beware), but are open to other design templates/printing companies as well. We just want to make sure its easy to find a print company to do our work. Too unique could be costly and hard to get cards printed.
• Colors to use: Our logo Blue (#006699), with either whites, grays, black, shades of our blue, and maybe a pinch of orange if needed. Primarily, blue, white, gray or black.
Nice to have
• Texture would be cool or little different edging or shape - but nothing too costly to print. I have seen cards with 3 sharp edges and one round edge. Something like that would be cool as an option. Or a vertical card.
• I love a faded watermark look. It would be nice to see some shading of our circle logo on a few designs. The circle with "hl" in it OR.... taking just the "hl" and using it alone.
Should not have
• No square card designs. Nothing too expensive or elaborate to print. No busy fonts. Do not like Times New Roman type fonts (too old looking). Not a lot of orange (if you even choose to use some orange).

```html
<!DOCTYPE html>
<html lang="en">
<head>
<meta charset="utf-8">
<title>Harbor Lantern IT business cards</title>
<link rel="stylesheet" href="https://fonts.googleapis.com/css2?family=Open+Sans:wght@400;600;700&display=swap">
<style>
  :root {
    --brand-blue: #1593cc;
    --brand-blue-deep: #0b6fa8;
    --brand-blue-light: #4db6e2;
    --ink: #474747;
    --ink-soft: #757575;
    --rule-grey: #555555;
    --card-white: #ffffff;
    --card-shade: #eef0f2;
    --backdrop: #e9e6e1;
  }
  html, body {
    margin: 0;
    width: 1200px;
    height: 1023px;
    overflow: hidden;
    background: var(--backdrop);
    font-family: "Open Sans", Arial, sans-serif;
  }
  .stage { position: relative; width: 1200px; height: 1023px; }

  .card {
    position: absolute;
    width: 620px;
    height: 360px;
    border-radius: 26px;
    overflow: hidden;
    box-shadow: 0 10px 26px rgba(0,0,0,0.18);
  }

  /* Front card */
  .card-front {
    left: 90px; top: 90px;
    background: linear-gradient(135deg, var(--card-white) 0%, var(--card-shade) 100%);
  }
  .card-front .swoosh { position: absolute; inset: 0; }
  .brand-name {
    position: absolute;
    left: 198px; top: 226px;
    margin: 0;
    font-size: 19px;
    font-weight: 600;
    color: var(--brand-blue-deep);
  }
  .contact {
    position: absolute;
    right: 34px; top: 30px;
    text-align: right;
    color: var(--ink);
    font-size: 14px;
    line-height: 1.45;
  }
  .contact p { margin: 0; }
  .contact .group { margin-bottom: 12px; }
  .contact .phone-row { display: flex; justify-content: flex-end; align-items: center; gap: 7px; }
  .contact .icon { width: 12px; height: 12px; flex: none; }
  .locations-title { color: var(--brand-blue); font-weight: 700; }
  .person {
    position: absolute;
    right: 34px; bottom: 30px;
    text-align: right;
  }
  .person-name { margin: 0; font-size: 18px; font-weight: 700; color: var(--brand-blue); }
  .person-role { margin: 0; font-size: 14px; color: var(--ink-soft); }

  /* Back card */
  .card-back {
    left: 490px; top: 575px;
    background: linear-gradient(160deg, var(--brand-blue-light) 0%, var(--brand-blue) 55%, var(--brand-blue-deep) 100%);
  }
  .card-back .texture { position: absolute; inset: 0; background: radial-gradient(circle at 50% 40%, rgba(255,255,255,0.12), rgba(255,255,255,0) 70%); }
  .back-brand {
    position: absolute;
    left: 0; right: 0; top: 140px;
    display: flex; justify-content: center; align-items: center; gap: 16px;
  }
  .back-brand .dot { width: 58px; height: 58px; border-radius: 50%; background: var(--card-white); }
  .back-brand .wordmark { margin: 0; font-size: 30px; font-weight: 600; color: var(--card-white); }
  .web {
    position: absolute;
    left: 34px; bottom: 26px;
    margin: 0;
    font-size: 15px;
    color: var(--card-white);
  }
</style>
</head>
<body>
<main class="stage">

  <section class="card card-front" aria-label="Business card front">
    <svg class="swoosh" viewBox="0 0 620 360" aria-hidden="true">
      <path d="M0 0 H170 C70 70 30 210 80 360 H0 Z" fill="var(--brand-blue)"/>
      <path d="M260 0 C110 60 60 230 150 360" fill="none" stroke="var(--brand-blue)" stroke-width="16"/>
      <path d="M230 0 C90 70 50 220 128 360" fill="none" stroke="var(--rule-grey)" stroke-width="7"/>
      <circle cx="112" cy="236" r="78" fill="var(--brand-blue)" stroke="var(--card-white)" stroke-width="8"/>
    </svg>
    <p class="brand-name">Harbor Lantern IT</p>

    <div class="contact">
      <div class="group">
        <p>7318 Quillby Avenue Suite</p>
        <p>F Alderton, CA 95871</p>
      </div>
      <div class="group">
        <p class="phone-row">530.555.0164
          <svg class="icon" viewBox="0 0 12 12"><rect x="3" y="0.5" width="6" height="11" rx="1.5" fill="var(--brand-blue)"/></svg></p>
        <p class="phone-row">530.555.0137 (Office)
          <svg class="icon" viewBox="0 0 12 12"><rect x="1" y="1" width="10" height="10" rx="1.5" fill="none" stroke="var(--brand-blue)" stroke-width="1.4"/></svg></p>
        <p class="phone-row">530.555.0182 (Direct)
          <svg class="icon" viewBox="0 0 12 12"><rect x="1" y="1" width="10" height="10" rx="1.5" fill="none" stroke="var(--brand-blue)" stroke-width="1.4"/></svg></p>
        <p class="phone-row">rtavener@hlit-example.com
          <svg class="icon" viewBox="0 0 12 12"><rect x="0.5" y="2" width="11" height="8" rx="1" fill="var(--brand-blue)"/><path d="M0.5 2.5 L6 7 L11.5 2.5" fill="none" stroke="var(--card-white)" stroke-width="1"/></svg></p>
      </div>
      <p class="locations-title">Locations Serviced:</p>
      <p>Alderton, Brookmere, Ridgeport, Fallow.</p>
    </div>

    <div class="person">
      <p class="person-name">Ross Tavener</p>
      <p class="person-role">Founder, CEO</p>
    </div>
  </section>

  <section class="card card-back" aria-label="Business card back">
    <div class="texture" role="img" aria-label="Soft repeating brand pattern across the blue card back"></div>
    <div class="back-brand">
      <span class="dot"></span>
      <p class="wordmark">Harbor Lantern IT</p>
    </div>
    <p class="web">www.hlit-example.com</p>
  </section>

</main>
</body>
</html>
```